TRU PEAK POWER.

I'd like my business logo.
contact name: Desmond Halvik
phone:0438275160
email: info@trupeakpower.net.au
website: www.trupeakpower.net.au

services:
solar
battery storage
LED lighting
energy saving solutions
general electrical
I'd like the design to look professional

Target Market(s)

Everyone

Industry/Entity Type

Business

Contact Information for Business Card

as described above

Requirements
Must have
• Id like the colours and the design to work well with my logo.

```html
<!DOCTYPE html>
<html lang="en">
<head>
<meta charset="utf-8">
<title>Tru Peak Power – Business Card</title>
<link href="https://fonts.googleapis.com/css2?family=Lato:wght@400;700&display=swap" rel="stylesheet">
<style>
  :root {
    --backdrop: #c9ccd0;
    --card-white: #ffffff;
    --green-light: #9cc935;
    --green-mid: #86b62a;
    --green-dark: #6aa11e;
    --brand-green: #5fae3c;
    --accent-orange: #f39a1e;
    --text-white: #ffffff;
    --divider: rgba(120, 160, 40, 0.7);
  }
  * { box-sizing: border-box; margin: 0; padding: 0; }
  html, body {
    width: 1200px; height: 1000px; overflow: hidden;
    background: var(--backdrop);
    font-family: "Lato", sans-serif;
  }
  .business-card {
    position: absolute; left: 100px; top: 220px;
    width: 1000px; height: 560px;
    background: var(--card-white);
    overflow: hidden;
  }
  .card-wave { position: absolute; left: 0; top: 0; width: 1000px; height: 560px; }
  .brand {
    position: absolute; left: 60px; top: 95px;
    display: flex; align-items: center; gap: 18px;
  }
  .brand-dot {
    width: 64px; height: 64px; border-radius: 50%;
    background: var(--brand-green);
  }
  .brand-name {
    font-weight: 700; font-size: 50px; color: var(--brand-green);
    letter-spacing: 1px;
  }
  .services {
    position: absolute; right: 40px; top: 40px;
    list-style: none; text-align: right;
    color: var(--accent-orange); font-size: 20px; line-height: 26px;
    letter-spacing: 1px; text-transform: uppercase;
  }
  .person { position: absolute; left: 50px; top: 318px; }
  .person-name { font-weight: 700; font-size: 52px; color: var(--text-white); line-height: 1.1; }
  .person-role { font-weight: 700; font-size: 22px; color: var(--accent-orange); }
  .divider {
    position: absolute; left: 445px; top: 295px;
    width: 2px; height: 190px; background: var(--divider);
  }
  .contacts { position: absolute; left: 475px; top: 300px; list-style: none; }
  .contact {
    display: flex; align-items: center; gap: 16px;
    height: 56px; font-size: 28px; color: var(--text-white);
  }
  .contact svg { width: 32px; height: 32px; flex: none; }
</style>
</head>
<body>
  <article class="business-card">
    <svg class="card-wave" viewBox="0 0 1000 560" aria-hidden="true">
      <path d="M0 180 C200 215 360 250 560 215 C720 185 880 160 1000 235 L1000 560 L0 560 Z" fill="var(--green-dark)"/>
      <path d="M0 205 C200 240 360 270 560 238 C720 212 880 195 1000 260 L1000 560 L0 560 Z" fill="var(--green-light)"/>
    </svg>

    <div class="brand">
      <span class="brand-dot"></span>
      <span class="brand-name">TRU PEAK POWER</span>
    </div>

    <ul class="services">
      <li>Solar</li>
      <li>Battery Storage</li>
      <li>LED Lighting</li>
      <li>Energy Saving Solutions</li>
    </ul>

    <div class="person">
      <p class="person-name">Desmond Halvik</p>
      <p class="person-role">Director</p>
    </div>

    <div class="divider"></div>

    <ul class="contacts">
      <li class="contact">
        <svg viewBox="0 0 32 32" aria-hidden="true"><rect x="3" y="7" width="26" height="18" fill="var(--accent-orange)"/><path d="M3 7 L16 18 L29 7" fill="none" stroke="#fff" stroke-width="1.6"/></svg>
        <span>info@trupeakpower.net.au</span>
      </li>
      <li class="contact">
        <svg viewBox="0 0 32 32" aria-hidden="true"><rect x="9" y="3" width="14" height="26" rx="2" fill="none" stroke="var(--accent-orange)" stroke-width="2.2"/><line x1="14" y1="25" x2="18" y2="25" stroke="var(--accent-orange)" stroke-width="2"/></svg>
        <span>0438 275 160</span>
      </li>
      <li class="contact">
        <svg viewBox="0 0 32 32" aria-hidden="true" fill="none" stroke="var(--accent-orange)" stroke-width="2"><circle cx="16" cy="16" r="12"/><ellipse cx="16" cy="16" rx="5" ry="12"/><line x1="4" y1="16" x2="28" y2="16"/></svg>
        <span>www.trupeakpower.net.au</span>
      </li>
    </ul>
  </article>
</body>
</html>
```